RW Frameworks Inc Business cards

We need business cards using our existing logo but slightly modified. Right now the logo says RW Framework Masonry. We want to keep the RW part of the design, but replace the Framework Masonry portion with "FRAMEWORKS". Please see the attached file.
Ideally this would be a blank template so we can add Different Names, titles, and phone numbers later.
On the one side we want only the logo and on the other side the detail. I'm attaching an example for you to see.
Please reach out with any other questions. Our address and other details will be given out once we find a design we like.

Target Market(s)

Construction Industry

```html
<!DOCTYPE html>
<html lang="en">
<head>
<meta charset="utf-8">
<title>RW Frameworks Inc – Business Cards</title>
<link rel="stylesheet" href="https://fonts.googleapis.com/css2?family=Montserrat:wght@400;500;700;800&display=swap">
<style>
  :root {
    --backdrop: #3b3c3f;
    --brand-blue: #1b75bc;
    --trim-blue: #a9cfea;
    --deep-blue: #0f72b8;
    --paper: #ffffff;
    --ink: #4a4a4a;
    --icon: #6d6e71;
    --sketch-a: #f4f5f7;
    --sketch-b: #e9ecf0;
  }
  * { margin: 0; padding: 0; box-sizing: border-box; }
  html, body {
    width: 1200px; height: 862px; overflow: hidden;
    background: var(--backdrop);
    font-family: "Montserrat", sans-serif;
  }
  .card {
    position: absolute;
    width: 620px; height: 354px;
    overflow: hidden;
    box-shadow: 0 10px 24px rgba(0,0,0,.35);
  }
  .card-trim { position: absolute; inset: 0; width: 100%; height: 100%; }

  /* Back side */
  .card-back { left: 60px; top: 60px; background: var(--brand-blue); }
  .card-back .brand {
    position: absolute; left: 0; right: 0; top: 120px;
    text-align: center;
  }
  .brand-name {
    display: inline-flex; align-items: center; gap: 14px;
    font-weight: 700; letter-spacing: 3px;
  }
  .brand-mark { width: 18px; height: 18px; border-radius: 50%; }
  .card-back .brand-name { color: var(--paper); font-size: 40px; }
  .card-back .brand-mark { background: var(--trim-blue); }
  .card-back .site {
    position: absolute; left: 0; right: 0; top: 268px;
    text-align: center; color: var(--paper);
    font-size: 12px; font-weight: 500; letter-spacing: .5px;
  }

  /* Front side */
  .card-front { left: 520px; top: 448px; background: var(--paper); }
  .sketch-area {
    position: absolute; right: 0; top: 0; width: 340px; height: 100%;
    background: linear-gradient(135deg, var(--sketch-b), var(--sketch-a) 60%, var(--paper));
    opacity: .8;
  }
  .card-front .brand { position: absolute; right: 44px; top: 96px; }
  .card-front .brand-name { color: var(--deep-blue); font-size: 30px; letter-spacing: 2px; gap: 10px; }
  .card-front .brand-mark { background: var(--icon); width: 14px; height: 14px; border-radius: 0; }

  .person { position: absolute; left: 78px; top: 150px; }
  .person-name { color: var(--deep-blue); font-size: 26px; font-weight: 800; line-height: 1.1; }
  .person-title { color: var(--ink); font-size: 17px; font-weight: 500; margin-top: 2px; }
  .contact-list { list-style: none; margin-top: 16px; }
  .contact-list li {
    display: flex; align-items: center; gap: 12px;
    color: var(--ink); font-size: 12px; font-weight: 500; height: 22px;
  }
  .contact-list svg { width: 15px; height: 15px; fill: var(--icon); flex: none; }
</style>
</head>
<body>

<section class="card card-back" aria-label="Business card, logo side">
  <svg class="card-trim" viewBox="0 0 620 354" preserveAspectRatio="none" aria-hidden="true">
    <polygon points="0,0 22,0 22,210 60,250 60,354 0,354" fill="var(--trim-blue)"/>
    <polygon points="0,0 10,0 10,205 48,250 48,354 0,354" fill="var(--brand-blue)" opacity="0"/>
    <polygon points="560,0 620,0 620,180 600,180 600,60 560,24" fill="var(--trim-blue)"/>
  </svg>
  <div class="brand">
    <span class="brand-name"><span class="brand-mark"></span>RW Frameworks</span>
  </div>
  <p class="site">www.rwframeworks.com</p>
</section>

<section class="card card-front" aria-label="Business card, contact side">
  <div class="sketch-area" role="img" aria-label="Faint architectural line sketch of a building facade"></div>
  <svg class="card-trim" viewBox="0 0 620 354" preserveAspectRatio="none" aria-hidden="true">
    <polygon points="0,150 18,150 48,180 48,354 0,354" fill="var(--deep-blue)"/>
    <polygon points="560,0 620,0 620,170 600,170 600,30 580,10" fill="var(--deep-blue)"/>
  </svg>
  <div class="brand">
    <span class="brand-name"><span class="brand-mark"></span>RW Frameworks</span>
  </div>
  <div class="person">
    <p class="person-name">Alex Morgan</p>
    <p class="person-title">Founder</p>
    <ul class="contact-list">
      <li>
        <svg viewBox="0 0 24 24" aria-hidden="true"><path d="M6.6 10.8a15.1 15.1 0 0 0 6.6 6.6l2.2-2.2a1 1 0 0 1 1-.25 11.4 11.4 0 0 0 3.6.57 1 1 0 0 1 1 1V20a1 1 0 0 1-1 1A17 17 0 0 1 3 4a1 1 0 0 1 1-1h3.5a1 1 0 0 1 1 1c0 1.25.2 2.45.57 3.57a1 1 0 0 1-.25 1z"/></svg>
        555-014-2260
      </li>
      <li>
        <svg viewBox="0 0 24 24" aria-hidden="true"><path d="M12 2a7 7 0 0 0-7 7c0 5.25 7 13 7 13s7-7.75 7-13a7 7 0 0 0-7-7zm0 9.5A2.5 2.5 0 1 1 12 6.5a2.5 2.5 0 0 1 0 5z"/></svg>
        412 Oakline Ave, Milford, PA 18337
      </li>
      <li>
        <svg viewBox="0 0 24 24" aria-hidden="true"><path d="M2 5h20v14H2zm2 2v.5l8 5 8-5V7zm0 2.8V17h16V9.8l-8 5z"/></svg>
        sales@rwframeworks.com
      </li>
      <li>
        <svg viewBox="0 0 24 24" aria-hidden="true"><path d="M12 2a10 10 0 1 0 0 20 10 10 0 0 0 0-20zm6.9 6h-3a15 15 0 0 0-1.3-3.9A8 8 0 0 1 18.9 8zM12 4c.9 1.2 1.6 2.6 2 4h-4c.4-1.4 1.1-2.8 2-4zM4.3 14a8 8 0 0 1 0-4h3.4a16 16 0 0 0 0 4zm.8 2h3a15 15 0 0 0 1.3 3.9A8 8 0 0 1 5.1 16zm3-8h-3a8 8 0 0 1 4.3-3.9A15 15 0 0 0 8.1 8zM12 20c-.9-1.2-1.6-2.6-2-4h4c-.4 1.4-1.1 2.8-2 4zm2.3-6H9.7a14 14 0 0 1 0-4h4.6a14 14 0 0 1 0 4zm.3 5.9a15 15 0 0 0 1.3-3.9h3a8 8 0 0 1-4.3 3.9zm1.7-5.9a16 16 0 0 0 0-4h3.4a8 8 0 0 1 0 4z"/></svg>
        www.rwframeworks.com
      </li>
    </ul>
  </div>
</section>

</body>
</html>
```